Design of an attractive membership brochure/membership card for an Electrical Business

Hi, we are an electrical business based in Sydney, Australia.

Our design's aim is to attract and target new customers into using our business as a repeat for anything electrical in their home. We would be handing this out to them after a job is completed and they're happy with the service.
We're thinking of a brochure, possibly additional membership cards with personalized number ID's for each client.

Open to ideas, but some of the things we want to include on our brochure are perks of why the client should sign up with us as a lifetime client
- Discounted emergency call out fees outside of normal hours
- Lifetime membership price, one time payment
- Exclusive 10% member discount on all future jobs
- Priority on any during business hour jobs or emergencies

If any other questions please don't hesitate to reach out.
We've attached our logo for reference for the mock designs.
Our website
https://brightwirecrew.com.au/

```html
<!DOCTYPE html>
<html lang="en">
<head>
<meta charset="utf-8">
<title>Bright Wire Crew – Membership Flyer</title>
<link href="https://fonts.googleapis.com/css2?family=Michroma&family=Quicksand:wght@500&family=Roboto:wght@400&display=swap" rel="stylesheet">
<style>
  :root {
    --brand-red: #e0332a;
    --ink: #1a1a1a;
    --paper: #ffffff;
    --backdrop: #e6e6e8;
    --photo-top: #b8322b;
    --photo-mid: #7d6f78;
    --photo-bottom: #c9ccd6;
  }
  html, body {
    margin: 0;
    width: 1199px;
    height: 1200px;
    overflow: hidden;
    background: var(--backdrop);
  }
  .flyer {
    position: absolute;
    left: 222px;
    top: 65px;
    width: 755px;
    height: 1070px;
    display: block;
    box-shadow: 0 6px 18px rgba(0,0,0,0.25);
  }
  .paper { fill: var(--paper); }
  .band-red { fill: var(--brand-red); }
  .band-black { fill: var(--ink); }
  .brand-name { font-family: "Michroma", sans-serif; fill: var(--brand-red); font-size: 20px; }
  .headline { font-family: "Michroma", sans-serif; fill: var(--paper); }
  .headline-small { font-size: 24px; }
  .headline-large { font-size: 54px; }
  .perk { font-family: "Quicksand", sans-serif; font-weight: 500; font-size: 12.5px; fill: #2a2a2a; }
  .perk-dot { fill: var(--ink); }
  .contact { font-family: "Roboto", sans-serif; font-size: 12.5px; fill: #2a2a2a; }
  .contact-icon { fill: var(--ink); }
</style>
</head>
<body>
<svg class="flyer" viewBox="0 0 604 856" xmlns="http://www.w3.org/2000/svg">
  <defs>
    <linearGradient id="houseTones" x1="0" y1="0" x2="0" y2="1">
      <stop offset="0" stop-color="var(--photo-top)"/>
      <stop offset="0.5" stop-color="var(--photo-mid)"/>
      <stop offset="0.75" stop-color="var(--photo-bottom)"/>
      <stop offset="1" stop-color="#dcdfe6"/>
    </linearGradient>
  </defs>

  <rect class="paper" x="0" y="0" width="604" height="856"/>

  <!-- top red chevron -->
  <polygon class="band-red" points="234,0 522,0 604,0 604,8 382,73"/>
  <polygon class="band-red" points="234,0 382,73 522,0"/>

  <!-- house photograph area -->
  <polygon role="img" aria-label="Photo of a two-storey suburban house with a white garage door" fill="url(#houseTones)" points="210,230 382,73 604,10 604,660 210,463"/>

  <!-- left red panel -->
  <polygon class="band-red" points="0,300 300,150 210,463 0,551"/>

  <!-- black stripes -->
  <polygon class="band-black" points="0,273 202,180 202,198 0,292"/>
  <polygon class="band-black" points="210,458 604,652 604,668 210,472"/>
  <polygon class="band-black" points="189,856 404,748 404,760 212,856"/>

  <!-- bottom red corner -->
  <polygon class="band-red" points="226,856 604,668 604,856"/>

  <!-- brand name -->
  <text class="brand-name" x="44" y="92">BRIGHT WIRE</text>
  <text class="brand-name" x="44" y="124">CREW</text>

  <!-- headline -->
  <text class="headline headline-small" x="37" y="323">BRIGHT WIRE</text>
  <text class="headline headline-large" x="37" y="390">CREW</text>

  <!-- perks -->
  <g class="perks">
    <circle class="perk-dot" cx="44" cy="563" r="3.6"/>
    <text class="perk" x="58" y="568">Discounted emergency call out fees</text>
    <text class="perk" x="58" y="587">outside of normal hours</text>

    <circle class="perk-dot" cx="44" cy="622" r="3.6"/>
    <text class="perk" x="58" y="627">Lifetime membership price, one time payment</text>

    <circle class="perk-dot" cx="44" cy="661" r="3.6"/>
    <text class="perk" x="58" y="666">Exclusive 10% member discount on all future jobs</text>

    <circle class="perk-dot" cx="44" cy="700" r="3.6"/>
    <text class="perk" x="58" y="705">Priority on any during business hour jobs or emergencies</text>
  </g>

  <!-- contact details -->
  <g class="contacts">
    <path class="contact-icon" d="M37,761 l3,-1 l2,3 l-1.5,1.5 q1.5,3 4,4 l1.5,-1.5 l3,2 l-1,3 q-7,-1 -11,-11 z"/>
    <text class="contact" x="58" y="771">135 246 780</text>

    <rect class="contact-icon" x="37" y="782" width="10" height="7"/>
    <text class="contact" x="58" y="791">info@brightwirecrew.com.au</text>

    <circle class="contact-icon" cx="42" cy="806" r="5"/>
    <text class="contact" x="58" y="811">www.brightwirecrew.com.au</text>
  </g>
</svg>
</body>
</html>
```